Psychiatrist/ Psychotherapist needs a letterhead design

I am a Psychiatrist working in private practice. I work as a psychotherapist and treat patients with depression, anxiety, post traumatic stress and relationship problems. I need a letterhead which is elegant and professional. I would like to see designs using colours such as blues and greys.
I would like the information on the letterhead split between the top and bottom of the page to give it a look of balance.
I want it to look elegant, feminine and upmarket. I don't want it to look too corporate but to show some flair and to be a bit artistic.

Target Market(s)

Other doctors, specialists and agencies who have referred patients to me.

Industry/Entity Type

Work

Font styles to use
Script

Requirements
Must have
• My name and my profession psychiatrist need to be highlighted and prominent. It needs to be professional looking and elegant without being old fashioned or too conservative.
Nice to have
• Balance between the top and bottom of the page.
Should not have
• I don't want fonts which are old and too traditional.

```html
<!DOCTYPE html>
<html lang="en">
<head>
<meta charset="utf-8">
<title>Letterhead – Dr Miriam Ashcombe</title>
<link href="https://fonts.googleapis.com/css2?family=Cinzel:wght@400;500;600&display=swap" rel="stylesheet">
<style>
  :root {
    --paper: #ffffff;
    --ink: #333333;
    --ornament: #3a3a3a;
  }
  html, body {
    margin: 0;
    padding: 0;
    overflow: hidden;
    background: var(--paper);
  }
  .letterhead {
    position: relative;
    width: 1200px;
    height: 1200px;
    background: var(--paper);
    color: var(--ink);
    font-family: "Cinzel", serif;
    overflow: hidden;
  }
  .branch-ornament {
    position: absolute;
    left: 530px;
    top: 42px;
    width: 190px;
    height: 160px;
  }
  .header {
    position: absolute;
    top: 220px;
    left: 0;
    width: 1240px;
    text-align: center;
  }
  .practitioner-name {
    margin: 0;
    font-size: 44px;
    font-weight: 600;
    letter-spacing: 2px;
    line-height: 52px;
  }
  .qualification {
    font-size: 27px;
    font-weight: 500;
    letter-spacing: 1px;
  }
  .profession {
    margin: 6px 0 0;
    font-size: 28px;
    font-weight: 500;
    letter-spacing: 2px;
    line-height: 36px;
  }
  .address {
    margin: 6px 0 0;
    font-size: 28px;
    font-weight: 500;
    letter-spacing: 2px;
    line-height: 36px;
  }
  .footer {
    position: absolute;
    top: 1166px;
    left: 0;
    width: 1240px;
    text-align: center;
  }
  .contact-line {
    margin: 0;
    font-size: 22px;
    font-weight: 600;
    letter-spacing: 1.5px;
    line-height: 32px;
    word-spacing: 2px;
  }
  .contact-line .gap { display: inline-block; width: 14px; }
  .email-line {
    margin: 0;
    font-size: 19px;
    font-weight: 600;
    letter-spacing: 2px;
    line-height: 30px;
    text-transform: lowercase;
  }
</style>
</head>
<body>
  <div class="letterhead">
    <svg class="branch-ornament" viewBox="0 0 190 160" role="img" aria-label="Decorative pair of willow branches arching towards each other">
      <rect x="0" y="0" width="190" height="160" rx="6" fill="var(--ornament)" opacity="0.85"/>
    </svg>

    <header class="header">
      <h1 class="practitioner-name">Dr Miriam Ashcombe <span class="qualification">B.Med,</span></h1>
      <p class="profession">FRANZCP Psychiatrist</p>
      <p class="address">14 Willow Lane, Norwood, SA 5067</p>
    </header>

    <footer class="footer">
      <p class="contact-line">Tel: (08) 8123 4501<span class="gap"></span> Fax: (08) 8123 4502<span class="gap"></span> Mobile: 0400123456</p>
      <p class="email-line">e-mail: mashcombe@mailnest.com.au</p>
    </footer>
  </div>
</body>
</html>
```